Landing page in the senior sector

We need a landing page for families looking for retirement homes for their parent. The target is rather old (50-60 years old). The mandatory fields are Name, Email, Phone. The optional fields are budget, research zipcode, Emergency (,,). It is important to note that this is a free service that we offer to families in research. It should be noted that they are often in distress and repulsive. Need a mobile landing We need a landing page to recruit families looking for retirement homes for their parent. The target is rather old (50-60 years old). Required fields are Name, Email, Phone. The optional fields (they may not appear at all) are Budget, Search CP, Emergency (,,). It is important to mention that this is a free service that we offer to families in search. It should be noted that they are often in distress and that asking them for input may let tel may seem repulsive. Also need a mobile version

Target Market(s)

rather old (50-60 years old) / rather old (50-60 years old)

Coding

Coded - Design and coding required

Number of Pages Required

2 page

Font styles to use
Sans Serif

Colors

Designer to choose colors to be used in the design.

Requirements
Must have
• - A form with the 3 mandatory fields / A form with the 3 mandatory fields - Optimized for conversion / Optimized for conversion

```html
<!DOCTYPE html>
<html lang="en">
<head>
<meta charset="utf-8">
<title>Evergreen Haven – Retirement Home Search</title>
<link href="https://fonts.googleapis.com/css2?family=Lato:wght@300;400;700;900&display=swap" rel="stylesheet">
<style>
  :root {
    --navy: #00478a;
    --navy-deep: #003c76;
    --blue: #0a78d8;
    --blue-mid: #0f6fc9;
    --lime: #b3d336;
    --ink: #0c4b8b;
    --mist: #eef0f2;
    --white: #ffffff;
    --text-grey: #555a60;
  }
  * { box-sizing: border-box; margin: 0; padding: 0; }
  html, body { width: 703px; height: 1200px; overflow: hidden; }
  body { font-family: 'Lato', Arial, sans-serif; background: var(--white); color: var(--white); }
  .page { position: relative; width: 703px; height: 1200px; overflow: hidden; }
  .band { position: absolute; left: 0; width: 703px; overflow: hidden; }
  .fill { position: absolute; inset: 0; }
  .abs { position: absolute; }

  /* Hero */
  .hero { top: 0; height: 278px; }
  .hero .photo-house { background: linear-gradient(160deg, #f6f7f8 0%, #e3e6e9 55%, #d8dcdf 100%); }
  .hero .photo-family { background: linear-gradient(150deg, #0a4f93 0%, #06407c 50%, #0b4a86 100%);
    clip-path: polygon(399px 0, 703px 0, 703px 100%, 302px 100%); }
  .brand { font-weight: 900; font-size: 10px; letter-spacing: .3px; color: var(--ink); display: flex; align-items: center; gap: 4px; white-space: nowrap; }
  .brand-mark { width: 8px; height: 8px; background: var(--lime); }
  .hero .brand { left: 179px; top: 36px; }
  .callout { right: 181px; top: 24px; text-align: right; }
  .callout-label { font-size: 6.7px; font-weight: 400; }
  .callout-number { font-size: 12px; font-weight: 700; color: var(--lime); margin-top: 1px; }
  .callout-rule { width: 21px; height: 2px; background: var(--white); margin: 4px 0 0 auto; }
  .kicker { font-size: 6.7px; font-weight: 400; }
  .display { font-size: 18px; font-weight: 900; line-height: 20px; text-transform: uppercase; margin-top: 3px; }
  .pitch-retire { left: 179px; top: 127px; color: #333; }
  .pitch-retire .display { color: var(--ink); }
  .pitch-family { left: 386px; top: 127px; }
  .pitch-family .display { color: var(--lime); }

  /* About */
  .about { top: 278px; height: 281px; }
  .about .photo-keys { background: linear-gradient(90deg, #f3f4f5 0%, #e9ebed 60%, #f1f2f3 100%); }
  .about .photo-swing { background: linear-gradient(160deg, #1f7fd6 0%, #0b6ccb 60%, #1a74cc 100%);
    clip-path: polygon(0 0, 302px 0, 399px 100%, 0 100%); }
  .welcome { left: 179px; top: 51px; width: 162px; }
  .welcome .display { color: var(--lime); }
  .welcome p { font-size: 5.8px; line-height: 8.4px; margin-top: 8px; }
  .btn { display: block; text-align: center; font-weight: 900; font-size: 5px; letter-spacing: 3px; color: var(--white); border: 0; white-space: nowrap; overflow: hidden; }
  .btn-read { width: 63px; height: 17px; line-height: 17px; background: var(--navy-deep); margin-top: 10px; }
  .offer-card { left: 360px; top: 52px; width: 163px; height: 176px; background: var(--navy); box-shadow: 0 4px 14px rgba(0,0,0,.25); text-align: center; padding-top: 8px; }
  .offer-title { font-size: 17px; font-weight: 900; line-height: 20px; }
  .offer-sub { font-size: 5.7px; margin-top: 6px; }
  .field { position: absolute; background: var(--white); color: #8a8f95; font-size: 5px; text-align: left; padding: 3px 4px; }
  .btn-agents { position: absolute; left: 17px; top: 143px; width: 128px; height: 17px; line-height: 17px; background: var(--blue); font-size: 4.8px; letter-spacing: 2px; }

  /* Gallery */
  .gallery { top: 559px; height: 279px; }
  .gallery .photo-walk { background: linear-gradient(90deg, #f1f2f3 0%, #e6e8ea 70%, #eceeef 100%); }
  .gallery .photo-street { background: linear-gradient(160deg, #0a4a8c 0%, #04407c 55%, #0a4c8a 100%);
    clip-path: polygon(399px 0, 703px 0, 703px 100%, 302px 100%); }
  .gallery-head { left: 0; width: 703px; top: 37px; text-align: center; }
  .gallery-head .kicker { color: var(--text-grey); }
  .gallery-head .display { color: var(--lime); }
  .card { top: 94px; width: 128px; height: 124px; background: var(--white); box-shadow: 0 3px 10px rgba(0,0,0,.18); }
  .card-photo { position: absolute; left: 4px; top: 4px; width: 120px; height: 96px; }
  .card-caption { position: absolute; left: 0; width: 100%; top: 105px; text-align: center; font-size: 6px; color: #333; letter-spacing: .2px; }
  .dots { left: 338px; top: 239px; display: flex; gap: 3.5px; }
  .dot { width: 3.5px; height: 3.5px; border-radius: 50%; border: .8px solid var(--white); }
  .dot.active { background: var(--white); }

  /* Contact */
  .contact { top: 838px; height: 280px; }
  .contact .photo-home { background: linear-gradient(180deg, #07457f 0%, #003e78 60%, #0a426f 100%); }
  .contact .photo-smile { background: linear-gradient(150deg, #1a82dd 0%, #0b72d2 55%, #167bd6 100%);
    clip-path: polygon(302px 0, 703px 0, 703px 100%, 399px 100%); }
  .contact-head { left: 0; width: 703px; top: 38px; text-align: center; }
  .contact-head .kicker { font-size: 7px; }
  .contact-head .display { font-size: 17.5px; margin-top: 4px; white-space: nowrap; }
  .contact-rule { width: 13px; height: 2px; background: var(--lime); margin: 5px auto 0; }
  .label { position: absolute; font-size: 5px; }
  .input { position: absolute; background: var(--white); color: #333; font-size: 5px; font-weight: 700; padding: 0 7px; display: flex; align-items: center; white-space: nowrap; }
  .input.area { align-items: flex-start; padding-top: 6px; }
  .input svg { position: absolute; right: 8px; }
  .btn-submit { position: absolute; left: 320px; top: 234px; width: 63px; height: 16px; line-height: 16px; background: var(--blue); }

  /* Footer */
  .footer { top: 1118px; height: 82px; background: var(--white); color: var(--text-grey); font-size: 5.5px; }
  .footer .copyright { left: 145px; top: 38px; }
  .footer .brand { left: 0; width: 703px; top: 34px; justify-content: center; }
  .footer .credit { right: 152px; top: 38px; }
  .footer .credit strong { color: var(--ink); font-weight: 700; }
</style>
</head>
<body>
<div class="page">

  <section class="band hero">
    <div class="fill photo-house" role="img" aria-label="Faded photo of a brick retirement house"></div>
    <div class="fill photo-family" role="img" aria-label="Blue-toned photo of grandparents with their grandchildren"></div>
    <div class="abs brand"><span class="brand-mark"></span>EVERGREEN HAVEN</div>
    <div class="abs callout">
      <div class="callout-label">Call Us Toll-Free</div>
      <div class="callout-number">000-000-0000</div>
      <div class="callout-rule"></div>
    </div>
    <div class="abs pitch-retire">
      <div class="kicker">Lorem Ipsum is simply</div>
      <h1 class="display">Retirement<br>Home</h1>
    </div>
    <div class="abs pitch-family">
      <div class="kicker">Lorem Ipsum is simply</div>
      <h2 class="display">Families<br>Looking</h2>
    </div>
  </section>

  <section class="band about">
    <div class="fill photo-keys" role="img" aria-label="Faded photo of keys hanging in a door lock"></div>
    <div class="fill photo-swing" role="img" aria-label="Blue-toned photo of a senior woman on a swing"></div>
    <div class="abs welcome">
      <div class="kicker">Welcome to</div>
      <h2 class="display">Evergreen<br>Haven</h2>
      <p>Lorem Ipsum is simply dummy text of the printing and typesetting industry. Lorem Ipsum has been the industry's standard dummy text ever since the 1500s, when an unknown printer took a galley of type and scrambled it to make a type specimen book.</p>
      <p>It has survived not only five centuries, but also the leap into electronic typesetting, remaining essentially unchanged. Lorem Ipsum is simply dummy text of the printing and typesetting industry. Lorem Ipsum has been the industry's standard dummy text ever since.</p>
      <span class="btn btn-read">READ MORE</span>
    </div>
    <div class="abs offer-card">
      <h2 class="offer-title">YOUR NEW<br>HOME AWAITS.</h2>
      <p class="offer-sub">Contact us to get the best offer from our agents!</p>
      <div class="field" style="left:17px;top:67px;width:128px;height:12px;">Name</div>
      <div class="field" style="left:17px;top:83px;width:63px;height:12px;">Email</div>
      <div class="field" style="left:82px;top:83px;width:63px;height:12px;">Phone</div>
      <div class="field" style="left:17px;top:99px;width:128px;height:37px;">Comment</div>
      <span class="btn btn-agents">CONTACT OUR AGENTS NOW!</span>
    </div>
  </section>

  <section class="band gallery">
    <div class="fill photo-walk" role="img" aria-label="Faded photo of a senior couple walking"></div>
    <div class="fill photo-street" role="img" aria-label="Blue-toned photo of a suburban house"></div>
    <div class="abs gallery-head">
      <div class="kicker">Evergreen Haven</div>
      <h2 class="display">Gallery</h2>
    </div>
    <div class="abs card" style="left:145px;">
      <div class="card-photo" role="img" aria-label="Stone house with lawn at dusk" style="background:linear-gradient(180deg,#8fa3b8 0%,#a68a6c 45%,#6f8a3e 75%,#b9b4aa 100%);"></div>
      <div class="card-caption">LOREM IPSUM IS SIMPLY</div>
    </div>
    <div class="abs card" style="left:287px;">
      <div class="card-photo" role="img" aria-label="Yellow Mediterranean villa with palm trees" style="background:linear-gradient(180deg,#3b8ee0 0%,#d9b84e 40%,#4f7a32 75%,#9a5a3e 100%);"></div>
      <div class="card-caption">LOREM IPSUM IS SIMPLY</div>
    </div>
    <div class="abs card" style="left:429px;">
      <div class="card-photo" role="img" aria-label="Single-storey family home with garage" style="background:linear-gradient(180deg,#6fa4d8 0%,#a9c7e6 40%,#c9a58a 60%,#5f8f34 85%,#cfcac0 100%);"></div>
      <div class="card-caption">LOREM IPSUM IS SIMPLY</div>
    </div>
    <div class="abs dots"><span class="dot active"></span><span class="dot"></span><span class="dot"></span><span class="dot"></span></div>
  </section>

  <section class="band contact">
    <div class="fill photo-home" role="img" aria-label="Dark blue-toned photo of a porch house"></div>
    <div class="fill photo-smile" role="img" aria-label="Blue-toned photo of a smiling senior woman"></div>
    <div class="abs contact-head">
      <div class="kicker">Contact Us</div>
      <h2 class="display">Schedule a Free Consultation</h2>
      <div class="contact-rule"></div>
    </div>
    <span class="label" style="left:188px;top:99px;">Name</span>
    <div class="input" style="left:188px;top:106px;width:161px;height:18px;">Frist Name</div>
    <span class="label" style="left:356px;top:99px;">Email</span>
    <div class="input" style="left:356px;top:106px;width:157px;height:18px;">@</div>
    <span class="label" style="left:188px;top:130px;">Phone</span>
    <div class="input" style="left:188px;top:137px;width:161px;height:18px;">+00 000 0000</div>
    <span class="label" style="left:356px;top:130px;">Select One Drop Down</span>
    <div class="input" style="left:356px;top:137px;width:157px;height:18px;">I'm interested in buying a home
      <svg width="5" height="3" viewBox="0 0 5 3"><path d="M0 0h5L2.5 3z" fill="#333"/></svg>
    </div>
    <span class="label" style="left:188px;top:164px;">Comment Box</span>
    <div class="input area" style="left:188px;top:171px;width:325px;height:49px;">Type Your Message Here</div>
    <span class="btn btn-submit">SUBMIT</span>
  </section>

  <footer class="band footer">
    <div class="abs copyright">© 2018 Evergreen Haven. All rights reserved.</div>
    <div class="abs brand"><span class="brand-mark"></span>EVERGREEN HAVEN</div>
    <div class="abs credit">Built By <strong>Northlight Studio</strong></div>
  </footer>

</div>
</body>
</html>
```